Single-sided business card for restaurant bellamonte with new logo made on this site

Business card options with new logo including restaurant name, address, phone number and website. This business card is single-sided only and will be presented at the hostess desk for clients to take. I would like to see options based on a cream card background, a white card background, a yellow card background and a burgundy colored background. It needs to be elegant and traditional.

Target Market(s)

local and international crowd

Industry/Entity Type

restaurant

Contact Information for Business Card

address, website and phone number

Font styles to use
Serif

Colors
EE7325
F08F49
F5BC92
FAE3D3
FDF4ED

Requirements
Must have
• new logo, address, phone number, website
Should not have
• more than three colors

```html
<!DOCTYPE html>
<html lang="es">
<head>
<meta charset="utf-8">
<title>Bellamonte – Tarjetas de presentación</title>
<link href="https://fonts.googleapis.com/css2?family=Source+Sans+3:wght@400;600&display=swap" rel="stylesheet">
<style>
  :root{
    --canvas:#8f8f8f;
    --yellow:#fbb040;
    --espresso:#3a1419;
    --burgundy:#7a1116;
    --cream:#fef9ec;
    --white:#ffffff;
  }
  *{margin:0;padding:0;box-sizing:border-box}
  html,body{width:727px;height:1200px;overflow:hidden;background:var(--canvas)}
  body{position:relative;font-family:"Source Sans 3",sans-serif}
  .card{position:absolute;left:104px;width:494px;height:282px;overflow:hidden;background:var(--bg);color:var(--ink)}
  .card--yellow{top:96px;--bg:var(--yellow);--band:var(--espresso);--ink:var(--espresso);--mark:var(--espresso);--icon:var(--cream)}
  .card--burgundy{top:458px;--bg:var(--burgundy);--band:var(--cream);--ink:var(--yellow);--mark:var(--white);--icon:var(--white)}
  .card--cream{top:820px;--bg:var(--cream);--band:var(--yellow);--ink:var(--espresso);--mark:var(--espresso);--icon:var(--yellow)}
  .band{position:absolute;background:var(--band)}
  .band--top{left:247px;top:0;width:247px;height:15px}
  .band--bottom{left:0;bottom:0;width:248px;height:17px}
  .brand{position:absolute;left:38px;top:66px;width:160px;text-align:center}
  .brand__square{display:block;width:81px;height:81px;margin:0 auto 10px;background:var(--mark)}
  .brand__name{font-weight:600;font-size:23px;line-height:25px;letter-spacing:5px;color:var(--mark);padding-left:5px}
  .info{position:absolute;left:248px;top:62px}
  .info__title{font-size:20px;font-weight:400;line-height:28px;margin-bottom:13px;white-space:nowrap}
  .info__row{position:relative;padding-left:32px;font-size:12.7px;line-height:19.5px;margin-bottom:7px;white-space:nowrap}
  .info__icon{position:absolute;left:0;top:3px;width:13px;height:14px;fill:none;stroke:var(--icon);stroke-width:1.3;stroke-linejoin:round;stroke-linecap:round}
</style>
</head>
<body>
<svg width="0" height="0" style="position:absolute">
  <symbol id="icon-phone" viewBox="0 0 16 16"><path d="M4 1.5l2.2 3-1.3 1.6c.8 1.9 2.4 3.5 4.3 4.3l1.6-1.3 3 2.2-1.3 2.6C7.6 14 2 8.4 1.5 3.3z"/><path d="M9.5 1.8a5 5 0 0 1 4.7 4.7M9.3 4.2a2.6 2.6 0 0 1 2.5 2.5"/></symbol>
  <symbol id="icon-pin" viewBox="0 0 16 16"><path d="M8 15s-5-5.2-5-8.7a5 5 0 0 1 10 0C13 9.8 8 15 8 15z"/><circle cx="8" cy="6.3" r="1.9"/></symbol>
  <symbol id="icon-pointer" viewBox="0 0 16 16"><path d="M3.5 1.5l9 6.2-4 .8 2.4 4.6-1.8.9-2.4-4.6-3.2 2.6z"/></symbol>
</svg>

<section class="card card--yellow">
  <div class="band band--top"></div><div class="band band--bottom"></div>
  <div class="brand"><span class="brand__square"></span><p class="brand__name">BELLA<br>MONTE</p></div>
  <div class="info">
    <h2 class="info__title">Restaurant Bellamonte</h2>
    <p class="info__row"><svg class="info__icon"><use href="#icon-phone"/></svg>Reservaciones 958-555-0142</p>
    <p class="info__row"><svg class="info__icon"><use href="#icon-pin"/></svg>Jacarandá 415<br>Bahías del Sol,<br>Oaxaca CP 70900</p>
    <p class="info__row"><svg class="info__icon"><use href="#icon-pointer"/></svg>www.bellamonte.com.mx</p>
  </div>
</section>

<section class="card card--burgundy">
  <div class="band band--top"></div><div class="band band--bottom"></div>
  <div class="brand"><span class="brand__square"></span><p class="brand__name">BELLA<br>MONTE</p></div>
  <div class="info">
    <h2 class="info__title">Restaurant Bellamonte</h2>
    <p class="info__row"><svg class="info__icon"><use href="#icon-phone"/></svg>Reservaciones 958-555-0142</p>
    <p class="info__row"><svg class="info__icon"><use href="#icon-pin"/></svg>Jacarandá 415<br>Bahías del Sol,<br>Oaxaca CP 70900</p>
    <p class="info__row"><svg class="info__icon"><use href="#icon-pointer"/></svg>www.bellamonte.com.mx</p>
  </div>
</section>

<section class="card card--cream">
  <div class="band band--top"></div><div class="band band--bottom"></div>
  <div class="brand"><span class="brand__square"></span><p class="brand__name">BELLA<br>MONTE</p></div>
  <div class="info">
    <h2 class="info__title">Restaurant Bellamonte</h2>
    <p class="info__row"><svg class="info__icon"><use href="#icon-phone"/></svg>Reservaciones 958-555-0142</p>
    <p class="info__row"><svg class="info__icon"><use href="#icon-pin"/></svg>Jacarandá 415<br>Bahías del Sol,<br>Oaxaca CP 70900</p>
    <p class="info__row"><svg class="info__icon"><use href="#icon-pointer"/></svg>www.bellamonte.com.mx</p>
  </div>
</section>
</body>
</html>
```